Shop Front face lift. We want to change our wholesale warehouse image into a retail superstore.

Brightcell Batteries sell Automotive 4x4 Truck Marine and Deep Cycle and other batteries. We need our shop front to reflect what we do. We are limited to only using the blue part on the front and side of the building. We can also use the windows on both sides including top and bottom. We want our shop front to stand out but most importantly let people know what we do.
Front Wall (entrance) Blue section 1325mm wide x 5080mm high. Front entrance Glass panels 3500mm wide x 5080mm high.

Side Wall (facing the road) Blue section 2050mm wide x 5080mm high. Side wall Glass panels 5900mm wide x 5080mm high.
Thank you

Target Market(s)

All passing traffic

Industry/Entity Type

Automotive

Colors
0054AA
0677BA
7BADD7
CADEEF
E8F1F8

Requirements
Must have
• We want our store front to pop, bright colours. Let people know we sell automotive 4x4 truck marine and deep cycle batteries and we are open to the public
Nice to have
• Some wow factor

```html
<!DOCTYPE html>
<html lang="en">
<head>
<meta charset="utf-8">
<title>Brightcell Batteries – Shop Front Signage</title>
<link rel="stylesheet" href="https://fonts.googleapis.com/css2?family=Bebas+Neue&family=Barlow+Condensed:ital,wght@1,800&family=Montserrat:wght@500;700;800&display=swap">
<style>
  :root {
    --backdrop: #3a3a3c;
    --blue: #1a5db8;
    --blue-deep: #0d47a3;
    --blue-shade: #0f4aa8;
    --blue-light: #2a6cc4;
    --white: #ffffff;
    --ink-blue: #1b4ea6;
  }
  * { margin: 0; padding: 0; box-sizing: border-box; }
  html, body { width: 1200px; height: 2625px; overflow: hidden; }
  body { background: var(--backdrop); position: relative; font-family: "Montserrat", sans-serif; color: var(--white); }

  .panel { position: absolute; background: var(--blue); overflow: hidden; box-shadow: 0 8px 24px rgba(0,0,0,.35); }
  .panel .bands { position: absolute; inset: 0; width: 100%; height: 100%; }

  /* Fascia sign */
  .fascia { left: 100px; top: 440px; width: 1000px; height: 560px; }
  .brand { position: absolute; left: 150px; top: 118px; display: flex; align-items: center; gap: 26px; }
  .brand-mark { width: 92px; height: 92px; background: var(--white); }
  .brand-name { font-family: "Montserrat", sans-serif; font-weight: 800; font-size: 62px; line-height: 60px; color: var(--white); letter-spacing: 2px; }
  .tagline { position: absolute; left: 150px; top: 322px; width: 700px; height: 70px; background: var(--white); transform: skewX(-12deg); display: flex; align-items: center; justify-content: center; box-shadow: 6px 6px 0 rgba(0,0,0,.12); }
  .tagline span { transform: skewX(12deg); font-family: "Barlow Condensed", sans-serif; font-style: italic; font-weight: 800; font-size: 46px; color: var(--ink-blue); }
  .web { position: absolute; left: 0; right: 0; top: 450px; text-align: center; font-size: 28px; letter-spacing: 5px; font-weight: 500; }
  .web b { font-weight: 800; }

  /* Lower panels */
  .intro { left: 100px; top: 1076px; width: 297px; height: 1110px; }
  .intro h2 { position: absolute; left: 46px; top: 50px; font-family: "Bebas Neue", sans-serif; font-weight: 400; font-size: 66px; line-height: 74px; }
  .contact { position: absolute; left: 46px; width: 208px; }
  .contact .rule-row { display: flex; align-items: center; gap: 12px; margin-bottom: 12px; }
  .contact .rule-row svg { width: 36px; height: 36px; flex: none; }
  .contact .rule-row i { flex: 1; height: 2px; background: var(--white); opacity: .85; }
  .contact p { font-weight: 700; font-size: 26px; line-height: 37px; }
  .contact.address { top: 540px; }
  .contact.phone { top: 772px; }

  .range { top: 1076px; width: 224px; height: 423px; }
  .range.r1 { left: 408px; background: var(--blue); }
  .range.r2 { left: 642px; background: var(--blue-shade); }
  .range.r3 { left: 876px; background: var(--blue-shade); }
  .range ul { list-style: none; position: absolute; left: 34px; top: 48px; width: 160px; }
  .range li { font-family: "Bebas Neue", sans-serif; font-size: 44px; line-height: 44px; }
  .range li:first-child { padding-bottom: 12px; border-bottom: 2px solid rgba(255,255,255,.85); margin-bottom: 22px; }
</style>
</head>
<body>

<section class="panel fascia" aria-label="Fascia sign">
  <svg class="bands" viewBox="0 0 1000 560" preserveAspectRatio="none" aria-hidden="true">
    <polygon points="0,240 300,0 380,0 0,330" fill="var(--blue-deep)" opacity=".55"/>
    <polygon points="60,110 170,40 170,230 60,300" fill="var(--blue-deep)" opacity=".45"/>
    <polygon points="850,560 1000,430 1000,500 930,560" fill="var(--blue-deep)" opacity=".6"/>
    <polygon points="760,560 1000,360 1000,390 800,560" fill="var(--blue-light)" opacity=".5"/>
  </svg>
  <div class="brand">
    <div class="brand-mark"></div>
    <div class="brand-name">BRIGHTCELL<br>BATTERIES</div>
  </div>
  <div class="tagline"><span>Quality Battery &amp; Power Solutions</span></div>
  <p class="web">WWW.<b>BRIGHTCELLBATTERIES</b>.COM.AU</p>
</section>

<section class="panel intro" aria-label="Side panel">
  <svg class="bands" viewBox="0 0 297 1110" preserveAspectRatio="none" aria-hidden="true">
    <polygon points="210,180 297,120 297,560 210,620" fill="var(--blue-deep)" opacity=".45"/>
    <polygon points="0,1110 297,820 297,900 80,1110" fill="var(--blue-light)" opacity=".35"/>
  </svg>
  <h2>We<br>provide a<br>quality<br>range of<br>batteries</h2>
  <div class="contact address">
    <div class="rule-row">
      <svg viewBox="0 0 36 36" aria-hidden="true"><circle cx="18" cy="18" r="17" fill="var(--white)"/><path d="M18 8a6 6 0 0 0-6 6c0 5 6 12 6 12s6-7 6-12a6 6 0 0 0-6-6z" fill="var(--blue)"/><circle cx="18" cy="14" r="2.2" fill="var(--white)"/></svg>
      <i></i>
    </div>
    <p>Unit 4/ 18<br>Harwick Loop<br>Ridgeview WA 6099<br>Australia</p>
  </div>
  <div class="contact phone">
    <div class="rule-row">
      <svg viewBox="0 0 36 36" aria-hidden="true"><circle cx="18" cy="18" r="17" fill="var(--white)"/><circle cx="18" cy="18" r="11" fill="none" stroke="var(--blue)" stroke-width="2"/><path d="M14 11c-2 1-2 4 0 7s5 6 8 6c2 0 3-2 2-3l-2-2-2 1c-1 0-3-2-4-4l1-2-2-3z" fill="var(--blue)"/></svg>
      <i></i>
    </div>
    <p>08 9471 2280<br>0400 517 362</p>
  </div>
</section>

<section class="panel range r1" aria-label="Automotive and truck">
  <svg class="bands" viewBox="0 0 224 423" preserveAspectRatio="none" aria-hidden="true">
    <polygon points="0,200 90,120 224,120 224,300 130,423 0,423" fill="var(--blue-deep)" opacity=".35"/>
  </svg>
  <ul><li>Automotive</li><li>Truck</li></ul>
</section>

<section class="panel range r2" aria-label="4x4 and deep cycle">
  <svg class="bands" viewBox="0 0 224 423" preserveAspectRatio="none" aria-hidden="true">
    <polygon points="170,240 224,180 224,423 120,423" fill="var(--blue-light)" opacity=".35"/>
  </svg>
  <ul><li>4×4</li><li>Deep Cycle</li></ul>
</section>

<section class="panel range r3" aria-label="Marine batteries">
  <svg class="bands" viewBox="0 0 224 423" preserveAspectRatio="none" aria-hidden="true">
    <polygon points="0,300 70,200 70,423 0,423" fill="var(--blue-deep)" opacity=".5"/>
  </svg>
  <ul><li>Marine</li><li>Batteries</li></ul>
</section>

</body>
</html>
```